Bookmark Design

We would like to design a book mark with logos of our two business and a quote.

One side with the quote "The first wealth is health" - Tobias Quill Harrow and the two logos.

The back side has the two logos with its respective phone numbers and a common address (this is to be advised to the winner of the project).

```html
<!DOCTYPE html>
<html lang="en">
<head>
<meta charset="utf-8">
<title>Bookmark Design – Maplewood Clinic &amp; Parkview Dental</title>
<link rel="stylesheet" href="https://fonts.googleapis.com/css2?family=Caveat+Brush&family=Encode+Sans+Semi+Condensed:wght@400;700&display=swap">
<style>
  :root {
    --page: #ffffff;
    --royal-blue: #0b47f5;
    --leaf-blue: #4a78f8;
    --card-grey: #e6e6e6;
    --leaf-grey: #eeeeee;
    --lime: #5fe83a;
    --slate: #3f4a4f;
    --white: #ffffff;
  }
  * { box-sizing: border-box; margin: 0; padding: 0; }
  html, body {
    width: 1200px; height: 1000px; overflow: hidden;
    background: var(--page);
    font-family: "Encode Sans Semi Condensed", Arial, sans-serif;
  }
  .bookmark {
    position: absolute; top: 119px;
    width: 254px; height: 762px;
    overflow: hidden;
  }
  .bookmark--front { left: 298px; background: var(--royal-blue); }
  .bookmark--back {
    left: 647px; background: var(--card-grey);
    box-shadow: 0 2px 6px rgba(0,0,0,0.12);
  }
  .leaf-pattern { position: absolute; inset: 0; }
  .bookmark--front .leaf-pattern {
    background: radial-gradient(ellipse at 55% 45%, var(--leaf-blue) 0%, rgba(74,120,248,0.55) 45%, rgba(11,71,245,0) 80%);
  }
  .bookmark--back .leaf-pattern {
    background: radial-gradient(ellipse at 50% 50%, var(--leaf-grey) 0%, rgba(238,238,238,0.6) 50%, rgba(230,230,230,0) 85%);
  }

  .quote {
    position: absolute; left: 0; right: 0;
    font-family: "Caveat Brush", cursive;
    color: var(--white); text-align: center; line-height: 1;
  }
  .quote__line { position: absolute; left: 0; right: 0; }
  .quote__the    { top: 168px; font-size: 58px; left: 30px; }
  .quote__first  { top: 210px; font-size: 100px; }
  .quote__wealth { top: 320px; font-size: 86px; }
  .quote__is     { top: 404px; font-size: 50px; left: -40px; }
  .quote__health { top: 430px; font-size: 92px; }
  .quote__author {
    position: absolute; top: 540px; right: 32px;
    font-family: "Caveat Brush", cursive;
    font-size: 18px; color: var(--white);
  }

  .front-brands {
    position: absolute; left: 0; right: 0; top: 668px;
    display: flex; justify-content: space-around; align-items: center;
    padding: 0 14px;
  }
  .brand-mark { display: flex; flex-direction: column; align-items: center; gap: 4px; }
  .brand-mark__dot {
    width: 38px; height: 38px; border-radius: 50%;
    border: 3px solid var(--white);
  }
  .brand-mark__name {
    font-weight: 700; font-size: 12px; color: var(--white);
    text-transform: uppercase; letter-spacing: 0.3px;
  }

  .clinic-brand {
    position: absolute; top: 60px; left: 0; right: 0;
    display: flex; flex-direction: column; align-items: center; gap: 10px;
  }
  .clinic-brand__ring {
    width: 100px; height: 100px; border-radius: 50%;
    border: 4px solid var(--royal-blue);
  }
  .clinic-brand__name {
    font-weight: 700; font-size: 23px; color: var(--royal-blue);
    text-transform: uppercase;
  }

  .contact { position: absolute; left: 0; right: 0; text-align: center; color: var(--royal-blue); }
  .contact__label { top: 272px; font-size: 12.5px; }
  .contact__phone { top: 292px; font-size: 30px; font-weight: 700; letter-spacing: 1px; }
  .contact__address { top: 384px; font-size: 18px; line-height: 1.35; }
  .contact__web { top: 483px; font-size: 18px; }

  .dental-brand {
    position: absolute; top: 630px; left: 0; right: 0;
    display: flex; justify-content: center; align-items: center; gap: 8px;
  }
  .dental-brand__square { width: 22px; height: 22px; background: var(--lime); }
  .dental-brand__name { font-weight: 700; font-size: 26px; color: var(--slate); }
</style>
</head>
<body>
  <section class="bookmark bookmark--front" aria-label="Bookmark front">
    <div class="leaf-pattern" role="img" aria-label="Large soft leaf pattern in lighter blue"></div>
    <blockquote class="quote">
      <span class="quote__line quote__the">The</span>
      <span class="quote__line quote__first">First</span>
      <span class="quote__line quote__wealth">Wealth</span>
      <span class="quote__line quote__is">is</span>
      <span class="quote__line quote__health">Health</span>
    </blockquote>
    <p class="quote__author">-Tobias Quill Harrow</p>
    <div class="front-brands">
      <div class="brand-mark">
        <span class="brand-mark__dot"></span>
        <span class="brand-mark__name">Maplewood Clinic</span>
      </div>
      <div class="brand-mark">
        <span class="brand-mark__name">Parkview Dental</span>
      </div>
    </div>
  </section>

  <section class="bookmark bookmark--back" aria-label="Bookmark back">
    <div class="leaf-pattern" role="img" aria-label="Faint leaf pattern in light grey"></div>
    <div class="clinic-brand">
      <span class="clinic-brand__ring"></span>
      <span class="clinic-brand__name">Maplewood Clinic</span>
    </div>
    <p class="contact contact__label">Appointments can be made by phone:</p>
    <p class="contact contact__phone">1234 5678</p>
    <p class="contact contact__address">12A Road Name<br>Street Name 3456</p>
    <p class="contact contact__web">www.websitename.com</p>
    <div class="dental-brand">
      <span class="dental-brand__square"></span>
      <span class="dental-brand__name">Parkview Dental</span>
    </div>
  </section>
</body>
</html>
```